Flyer-Design für Gesundheitskonzepte
Zielgruppe
Gesundheitskonzepte
Gesunde Unternehmenskultur
Wir schaffen ganzheitliche Gesundheitskonzepte von denen jeder Mitarbeiter profitiert!
Fördergelder für die Gesundheit der Mitarbeiter
Aufgabenstellung
Alles Details findet Ihr auf der Webseite www.haldenbach.org
BILD von mir sollte dabei sein (Kann ich mailen)
Schwerpunkt sollten Inhalte aus der Startseite 'HOME' sein
Siegel von Wohlhaus

```html
<!DOCTYPE html>
<html lang="de">
<head>
<meta charset="utf-8">
<title>Haldenbach Gesundheitskonzepte – Flyer</title>
<link href="https://fonts.googleapis.com/css2?family=Montserrat:ital,wght@0,400;0,500;0,600;0,700;1,600;1,700&display=swap" rel="stylesheet">
<style>
:root{
  --navy:#434b64;
  --navy-deep:#3a4159;
  --gold:#c3a56e;
  --gold-light:#d9c193;
  --paper:#ffffff;
  --paper-grey:#f3f3f4;
  --text-grey:#707480;
  --backdrop:#e8e8e9;
  --photo-a:#d7d9dd;
  --photo-b:#9fa4ae;
}
*{box-sizing:border-box;margin:0;padding:0}
html,body{width:667px;height:1200px;overflow:hidden}
body{background:var(--backdrop);font-family:"Montserrat",sans-serif;position:relative;color:var(--navy)}
.sheet{position:absolute;left:20px;width:627px;height:443px;display:flex;box-shadow:0 6px 18px rgba(0,0,0,.12)}
.sheet--outside{top:105px}
.sheet--inside{top:652px}
.panel{position:relative;width:209px;height:100%;overflow:hidden}
.panel--white{background:linear-gradient(180deg,var(--paper-grey),var(--paper))}
.panel--navy{background:var(--navy);color:#fff}

/* wordmark */
.wordmark{display:flex;align-items:center;gap:6px;justify-content:center}
.wordmark__dot{width:20px;height:20px;border-radius:50%;background:var(--navy)}
.panel--navy .wordmark__dot{background:#fff}
.wordmark__name{font-weight:700;font-size:17px;letter-spacing:.5px;line-height:1}
.wordmark__tag{font-size:5.6px;letter-spacing:2px;color:var(--gold);font-weight:600;margin-top:2px}

/* outside left */
.intro{padding:26px 16px 0}
.kicker{font-size:5px;color:var(--gold);font-weight:600;text-align:center;letter-spacing:.6px}
.headline{font-size:10px;font-weight:700;text-align:center;line-height:1.2;margin-top:3px;text-transform:uppercase}
.section-title{font-size:9px;color:var(--gold);font-weight:700;margin-top:14px;display:flex;align-items:center;gap:6px}
.section-title::after{content:"";flex:1;height:.6px;background:var(--gold-light)}
.body-text{font-size:5.6px;line-height:1.55;color:var(--text-grey);margin-top:4px}
.claim{font-size:6px;color:var(--text-grey);margin-top:10px}
.cta{font-size:6.2px;font-weight:700;margin-top:8px}
.callbox{margin-top:6px;border:.8px solid var(--gold);display:flex;align-items:center;gap:10px;padding:6px 10px;font-size:6.2px;font-weight:600;color:var(--gold);line-height:1.5}
.callbox svg{width:14px;height:14px;flex:none}

/* outside middle */
.contact{padding:30px 14px 0;text-align:center}
.contact-list{list-style:none;margin-top:20px}
.contact-list li{font-size:6px;line-height:1.45;margin-bottom:11px}
.contact-list strong{font-weight:600}
.contact-list svg{display:block;margin:0 auto 3px;width:9px;height:9px}
.web{border:.8px solid var(--gold);color:var(--gold);font-size:10px;font-weight:600;padding:7px 0;margin:10px 8px 0;letter-spacing:.4px}
.cta--light{color:#fff;margin-top:16px;font-size:6.2px}
.callbox--filled{background:var(--gold);color:#fff;border:none;margin:6px 8px 0;justify-content:center}

/* cover */
.cover-logo{position:absolute;top:18px;left:0;right:0;text-align:center;z-index:2}
.cover-photo{position:absolute;top:56px;left:0;width:209px;height:210px;background:linear-gradient(160deg,var(--photo-a),var(--photo-b))}
.cover-curve{position:absolute;top:220px;left:0;width:209px;height:223px}
.seal{position:absolute;border-radius:50%;background:radial-gradient(circle,#fff 0 55%,var(--gold) 57% 100%);box-shadow:0 0 0 2px var(--gold-light)}
.cover .seal{width:58px;height:58px;left:112px;top:236px}
.cover-text{position:absolute;top:340px;left:0;right:0;text-align:center;color:#fff}
.cover-text h2{font-size:10px;font-weight:600;font-style:italic;line-height:1.35}
.cover-text p{font-size:5.6px;color:var(--gold);font-weight:600;margin-top:6px;letter-spacing:.4px}

/* inside left */
.strip-photo{position:absolute;top:0;left:0;width:209px;height:92px;background:linear-gradient(150deg,var(--photo-b),var(--photo-a))}
.strip-curve{position:absolute;top:60px;left:0;width:209px;height:40px}
.story{position:absolute;top:108px;left:16px;right:14px}
.story .body-text{margin-top:8px}
.story .section-title{margin-top:12px}

/* inside middle */
.services{padding:22px 18px 0;text-align:center}
.service{padding-bottom:16px;margin-bottom:16px;border-bottom:.6px solid rgba(255,255,255,.25)}
.service:last-child{border:none}
.service svg{width:18px;height:18px;display:block;margin:0 auto 6px}
.service h3{font-size:8.5px;font-weight:600;letter-spacing:.6px}
.service p{font-size:5.6px;line-height:1.55;margin-top:6px}

/* inside right */
.about{padding:24px 16px 0}
.about h2{font-size:9px;font-weight:700;font-style:italic;line-height:1.3;text-align:center}
.about .kicker{margin-top:4px}
.about .body-text{margin-top:7px}
.portrait{position:absolute;bottom:0;left:0;width:209px;height:120px;background:linear-gradient(120deg,#b09a76,#5c5a5e)}
.portrait-curve{position:absolute;bottom:100px;left:0;width:209px;height:30px}
.about-seal{width:44px;height:44px;left:28px;bottom:62px}
.name-tag{position:absolute;right:10px;bottom:14px;background:var(--gold);color:#fff;font-size:7px;font-weight:600;padding:4px 10px}
</style>
</head>
<body>

<!-- Aussenseite -->
<section class="sheet sheet--outside">
  <article class="panel panel--white">
    <div class="intro">
      <p class="kicker">GESUNDHEIT. EINFACH. MACHEN.</p>
      <h2 class="headline">Damit Ihr Unternehmen<br>erfolgreich ist!</h2>
      <h3 class="section-title">Gesundheitsbewusstsein</h3>
      <p class="body-text">Wie Du durch Challenges, Gamification, besondere Events und monetäre Anreize ein Gesundheitsbewusstsein in Deinem Unternehmen schaffst, um Mitarbeiter &amp; Bewerber emotional zu begeistern und zu binden, damit Du als Arbeitgeber einzigartig wirkst – ohne jemals mehr verglichen zu werden.</p>
      <h3 class="section-title">Gesundheitsleistungen</h3>
      <p class="body-text">Wie Du gesetzlich geförderte Gesundheitsleistungen Deinen Mitarbeitern digitalisiert und verwaltungsarm zur Verfügung stellst, um einen spürbaren Benefit-Effekt zu verursachen, damit die Belegschaft permanent davon profitiert – ohne Leistungen emotional verpuffen zu lassen.</p>
      <h3 class="section-title">Gesundheitsbewusstsein</h3>
      <p class="body-text">Wie Du ein Gesundheitskonzept nachhaltig implementierst, um einen spürbaren Wow-Effekt über Zeit und Dauer zu verursachen, damit Deine Mitarbeiter und sogar (Mit-)Bewerber von Deinem Unternehmen schwärmen – ohne es jemals zu vergessen.</p>
      <p class="claim">Einfach. Verwaltungsarm. Digitalisiert. Gesetzlich gefördert.</p>
      <p class="cta">Vereinbaren Sie jetzt Ihr kostenloses Erstgespräch</p>
      <div class="callbox">
        <svg viewBox="0 0 24 24" fill="var(--gold)"><path d="M6.6 10.8a15.1 15.1 0 0 0 6.6 6.6l2.2-2.2a1 1 0 0 1 1-.25 11.4 11.4 0 0 0 3.6.57 1 1 0 0 1 1 1V20a1 1 0 0 1-1 1A17 17 0 0 1 3 4a1 1 0 0 1 1-1h3.5a1 1 0 0 1 1 1c0 1.25.2 2.45.57 3.57a1 1 0 0 1-.25 1z"/></svg>
        <span>Altmoor: +49 4000 12 345 67<br>Weserhafen: +49 400 98 76 54 32</span>
      </div>
    </div>
  </article>

  <article class="panel panel--navy">
    <div class="contact">
      <div class="wordmark"><span class="wordmark__dot"></span><span class="wordmark__name">HALDENBACH</span></div>
      <p class="wordmark__tag">GESUNDHEITSKONZEPTE</p>
      <ul class="contact-list">
        <li><svg viewBox="0 0 24 24" fill="#fff"><circle cx="12" cy="7" r="5"/><path d="M2 22c0-5 4.5-8 10-8s10 3 10 8z"/></svg><strong>Haldenbach Gesundheitskonzepte</strong></li>
        <li><svg viewBox="0 0 24 24" fill="#fff"><path d="M12 2a7 7 0 0 0-7 7c0 5 7 13 7 13s7-8 7-13a7 7 0 0 0-7-7zm0 9.5A2.5 2.5 0 1 1 12 6.5a2.5 2.5 0 0 1 0 5z"/></svg>Lindenweg 14<br>27311 Altmoor</li>
        <li><svg viewBox="0 0 24 24" fill="#fff"><path d="M6.6 10.8a15.1 15.1 0 0 0 6.6 6.6l2.2-2.2a1 1 0 0 1 1-.25 11.4 11.4 0 0 0 3.6.57 1 1 0 0 1 1 1V20a1 1 0 0 1-1 1A17 17 0 0 1 3 4a1 1 0 0 1 1-1h3.5a1 1 0 0 1 1 1c0 1.25.2 2.45.57 3.57a1 1 0 0 1-.25 1z"/></svg><strong>Standort Altmoor</strong><br>Telefon: 04000 1234567</li>
        <li><svg viewBox="0 0 24 24" fill="#fff"><path d="M6.6 10.8a15.1 15.1 0 0 0 6.6 6.6l2.2-2.2a1 1 0 0 1 1-.25 11.4 11.4 0 0 0 3.6.57 1 1 0 0 1 1 1V20a1 1 0 0 1-1 1A17 17 0 0 1 3 4a1 1 0 0 1 1-1h3.5a1 1 0 0 1 1 1c0 1.25.2 2.45.57 3.57a1 1 0 0 1-.25 1z"/></svg><strong>Standort Weserhafen</strong><br>Telefon: 0400 98765432</li>
        <li><svg viewBox="0 0 24 24" fill="#fff"><path d="M2 5h20v14H2z"/><path d="M2 5l10 8 10-8" stroke="var(--navy)" stroke-width="2" fill="none"/></svg>kontakt@haldenbach.org</li>
      </ul>
      <p class="web">www.haldenbach.org</p>
      <p class="cta cta--light">Vereinbaren Sie jetzt Ihr kostenloses Erstgespräch</p>
      <div class="callbox callbox--filled">
        <svg viewBox="0 0 24 24" fill="#fff"><path d="M6.6 10.8a15.1 15.1 0 0 0 6.6 6.6l2.2-2.2a1 1 0 0 1 1-.25 11.4 11.4 0 0 0 3.6.57 1 1 0 0 1 1 1V20a1 1 0 0 1-1 1A17 17 0 0 1 3 4a1 1 0 0 1 1-1h3.5a1 1 0 0 1 1 1c0 1.25.2 2.45.57 3.57a1 1 0 0 1-.25 1z"/></svg>
        <span>Altmoor: +49 4000 12 345 67<br>Weserhafen: +49 400 98 76 54 32</span>
      </div>
    </div>
  </article>

  <article class="panel panel--white cover">
    <div class="cover-logo">
      <div class="wordmark"><span class="wordmark__dot"></span><span class="wordmark__name">HALDENBACH</span></div>
      <p class="wordmark__tag">GESUNDHEITSKONZEPTE</p>
    </div>
    <div class="cover-photo" role="img" aria-label="Foto: Team im Büro legt die Hände übereinander"></div>
    <svg class="cover-curve" viewBox="0 0 209 223" preserveAspectRatio="none">
      <path d="M0 40 Q105 0 209 30 L209 223 L0 223 Z" fill="var(--navy)"/>
      <path d="M0 38 Q105 -2 209 28" stroke="var(--gold)" stroke-width="2" fill="none"/>
    </svg>
    <div class="seal" role="img" aria-label="Siegel Wohlhaus-Zertifikat"></div>
    <div class="cover-text">
      <h2>Gemeinsam schaffen wir Eure<br>gesunde Unternehmenskultur!</h2>
      <p>WIR FREUEN UNS AUF EUCH</p>
    </div>
  </article>
</section>

<!-- Innenseite -->
<section class="sheet sheet--inside">
  <article class="panel panel--white">
    <div class="strip-photo" role="img" aria-label="Foto: übereinandergelegte Hände des Teams"></div>
    <svg class="strip-curve" viewBox="0 0 209 40" preserveAspectRatio="none">
      <path d="M0 12 Q110 40 209 22 L209 40 L0 40 Z" fill="var(--paper-grey)"/>
      <path d="M0 12 Q110 40 209 22" stroke="var(--gold)" stroke-width="1.5" fill="none"/>
    </svg>
    <div class="story">
      <p class="body-text">Wir zeigen dir wie Du Dich als Arbeitgeber, durch ein ganzheitliches Gesundheitskonzept, systematisch vom Mitbewerber abhebst und Deine Mitarbeiter emotional, nachhaltig und messbar motivierst.</p>
      <p class="body-text">Als Experte für innovative Gesundheitskonzepte durfte ich über eine Kooperation und über eine Empfehlung eines langjährigen Geschäftspartners das Unternehmen Wohlhaus kennenlernen. Ich bin stolzer Teil der Wohlhaus-Community aus Unternehmen und Beratern, deren Vision die Schaffung gesunder Unternehmenskulturen ist.</p>
      <p class="body-text">Gemeinsam mit unseren Partnern haben wir die Erfahrung aus über 10.000 Projekten gesammelt und die bewährten Vorgehensweisen und Dienstleistungen zu einem ganzheitlichen Konzept kombiniert und weiterentwickelt.</p>
      <h3 class="section-title">Das Ergebnis:</h3>
      <p class="body-text">Ein holistisches Gesundheitskonzept mit 2500 flexibel abrufbaren Leistungen, das stetig weiterentwickelt wird. Für die Finanzierung verwenden wir Fördergelder, die über 90% der Unternehmen verfallen lassen. Wir zeigen, was es für Gelder gibt und rufen sie direkt für das Unternehmen ab. Ohne Verwaltungsaufwand für das Unternehmen.</p>
      <p class="body-text">In einer Erstberatung, inklusive Fördermittelcheck finden wir gemeinsam heraus, wie wir Dich und Dein Unternehmen bei der Entwicklung einer gesunden Unternehmenskultur unterstützen können!</p>
    </div>
  </article>

  <article class="panel panel--navy">
    <div class="services">
      <div class="service">
        <svg viewBox="0 0 24 24"><path d="M3 13l6 6L21 6" stroke="var(--gold)" stroke-width="3" fill="none"/></svg>
        <h3>FÖRDERCHECK</h3>
        <p>In einem persönlichen 15 – 30 minütigen kostenfreien Telefongespräch machen wir eine erste Bestandsaufnahme der aktuellen Gesundheitsleistungen und prüfen die Fördermöglichkeiten.</p>
      </div>
      <div class="service">
        <svg viewBox="0 0 24 24" fill="var(--gold)"><path d="M2 3h13v9H7l-4 3v-3H2z"/><path d="M17 8h5v9h-1v3l-4-3h-7v-3h7z"/></svg>
        <h3>BERATUNG</h3>
        <p>Sind die Voraussetzungen erfüllt, geht es in einen 60 – 90 minütigen Videocall mit einem unserer Berater, der mit Dir/Euch gemeinsam ein förderfähiges Gesundheitskonzept und ein Schritt für Schritt Plan zur Umsetzung erstellt.</p>
      </div>
      <div class="service">
        <svg viewBox="0 0 24 24" fill="var(--gold)"><circle cx="9" cy="7" r="4"/><path d="M1 21c0-5 3.5-8 8-8s8 3 8 8z"/><circle cx="17" cy="6" r="3"/><path d="M17 11c3.5 0 6 2.5 6 7h-4c-.5-3-1.5-5-3.5-6.5z"/></svg>
        <h3>MEMBERBEREICH</h3>
        <p>Bei einer Zusammenarbeit werdet Ihr Teil unserer Wohlhaus-Community. Wir begleiten Euch zu einer gesunden Unternehmenskultur voller Anerkennung, Wertschätzung und Gesundheitsleistungen, welche die Mitarbeiter auch nutzen.</p>
      </div>
    </div>
  </article>

  <article class="panel panel--white">
    <div class="about">
      <h2>Gemeinsam schaffen wir Eure<br>gesunde Unternehmenskultur!</h2>
      <p class="kicker">MARKUS HALDENBACH · TEAM</p>
      <p class="body-text">Wir schaffen ganzheitliche Gesundheitskonzepte von denen jeder Mitarbeiter profitiert!</p>
      <p class="body-text">Gemeinsam mit einem Kreis von Spezialisten aus den Bereichen Personal, Arbeitgebermarketing, Recruiting, Förderungs- und Gesundheitsmanagement, Steuerberatung, Beratungsunternehmen zur Lohngestaltung, Kommunikationsdienstleister und diversen Gesundheitsinstituten habe ich bestehende Erfahrungen und Wissen gebündelt mit der Zielsetzung Gesundheitskonzepte aus Konzernen auch den mittelständischen Unternehmen zu ermöglichen.</p>
      <p class="body-text">Dabei profitiert das Konzept von der ständigen Weiterentwicklung des deutschlandweiten Partnernetzwerkes und den Erfahrungen der besten Arbeitgeber.</p>
      <p class="body-text">Wir unterstützen jedes Unternehmen durch Kommunikations-, Konflikt- und Changemanagement in ihrem Prozess, damit eine gesunde Unternehmenskultur nachhaltig gefestigt wird.</p>
    </div>
    <div class="portrait" role="img" aria-label="Porträtfoto von Markus Haldenbach im Treppenhaus"></div>
    <svg class="portrait-curve" viewBox="0 0 209 30" preserveAspectRatio="none">
      <path d="M0 30 Q100 2 209 10" stroke="var(--gold)" stroke-width="2" fill="none"/>
    </svg>
    <div class="seal about-seal" role="img" aria-label="Siegel Wohlhaus-Zertifikat"></div>
    <p class="name-tag">Markus Haldenbach</p>
  </article>
</section>

</body>
</html>
```